Book cover needed for a major new book on emotional resilience

The book will be titled: 'Storm to Stillness: from rigid habits to pioneers of renewal - The handbook for building steady teams and institutions'
My websites are http://www.brightmarrow.com and http://www.hollenquay.org and I am http://en.pedialoom.org/wiki/Tomas_Brenhurst_(uncertainty_scholar) ad expert in developing emotional resilience. My previous book was The Quiet Compass.
The premise of the book is to introduce brand new material which is the first ever methodology and strategy on how to develop emotional resilience across entire populations like organisations and companies or moving people from fear about change to finding flow through resilience.
The final design should communicate the fact that this is a strategy and methodology. That it is about developing people and entire organisations to be more resilient and who are able to deal with change better.
Target Market(s)
Consultants, Organisational development consultants, Human Resource professionals.

```html
<!DOCTYPE html>
<html lang="en">
<head>
<meta charset="utf-8">
<title>Storm to Stillness — Tomas Brenhurst</title>
<link href="https://fonts.googleapis.com/css2?family=Arimo:wght@400;700&display=swap" rel="stylesheet">
<style>
  :root {
    --bg: #d9d9d9;
    --white: #ffffff;
    --ink: #2b2b2b;
    --tint-warm: rgba(227, 37, 43, 0.18);
    --tint-cool: rgba(27, 169, 225, 0.20);
    --tint-deep: rgba(44, 47, 134, 0.16);
    --tint-sun: rgba(243, 229, 0, 0.26);
  }
  html, body {
    margin: 0;
    padding: 0;
    overflow: hidden;
  }
  .cover {
    position: relative;
    width: 750px;
    height: 1200px;
    background: var(--bg);
    overflow: hidden;
    font-family: "Arimo", Arial, sans-serif;
  }

  .decor {
    position: absolute;
    border-radius: 50%;
  }
  .decor--top-left {
    left: 10px; top: 10px; width: 320px; height: 320px;
    background: radial-gradient(circle, var(--tint-warm), var(--tint-deep) 55%, transparent 72%);
  }
  .decor--top-right {
    left: 500px; top: 20px; width: 150px; height: 120px;
    background: radial-gradient(circle, var(--tint-cool), transparent 70%);
  }
  .decor--bottom-left {
    left: 60px; top: 840px; width: 160px; height: 130px;
    background: radial-gradient(circle, var(--tint-deep), transparent 70%);
  }
  .decor--bottom-right {
    left: 420px; top: 890px; width: 280px; height: 170px;
    background: radial-gradient(circle, var(--tint-sun), var(--tint-warm) 45%, transparent 72%);
  }

  .author {
    position: absolute;
    top: 150px;
    left: 400px;
    width: 280px;
    margin: 0;
    text-align: center;
    color: var(--white);
    font-size: 34px;
    font-weight: 400;
    line-height: 40px;
  }

  .book-title {
    position: absolute;
    top: 372px;
    left: 0;
    width: 750px;
    margin: 0;
    text-align: center;
    font-weight: 700;
    color: transparent;
    -webkit-text-stroke: 2px var(--ink);
  }
  .book-title__line {
    display: block;
    font-size: 122px;
    line-height: 150px;
    letter-spacing: 14px;
  }
  .book-title__line--long {
    font-size: 100px;
    letter-spacing: 4px;
  }

  .tagline {
    position: absolute;
    top: 1060px;
    left: 40px;
    width: 670px;
    margin: 0;
    text-align: center;
    color: var(--white);
    font-size: 26px;
    line-height: 33px;
  }
</style>
</head>
<body>
<main class="cover">
  <div class="decor decor--top-left" role="img" aria-label="Scattered colourful outlined letters"></div>
  <div class="decor decor--top-right" role="img" aria-label="Scattered colourful outlined letter"></div>
  <div class="decor decor--bottom-left" role="img" aria-label="Scattered colourful outlined letter"></div>
  <div class="decor decor--bottom-right" role="img" aria-label="Scattered colourful outlined letters"></div>

  <p class="author">Tomas Brenhurst</p>

  <h1 class="book-title">
    <span class="book-title__line">STORM</span>
    <span class="book-title__line">TO</span>
    <span class="book-title__line book-title__line--long">STILLNESS</span>
  </h1>

  <p class="tagline">
    From rigid habits to pioneers of renewal<br>
    The handbook for building steady teams and<br>
    institutions
  </p>
</main>
</body>
</html>
```